Paint my screen with vibrant colors

I have got a screen for which the layout is kind of ready. I am looking for designs that are colored on top of this screen.

Target Market(s)

Storage administrator at public or private cloud

Requirements
Must have
• Matching icon themes
Matching button themes
Should not have
• I have uploaded the current screen .. your new design should be different than this one. We are trying to revamp the existing UI to the something more elegant and vibrant in colors.

```html
<!DOCTYPE html>
<html lang="en">
<head>
<meta charset="utf-8">
<title>Stratus Console – Admin</title>
<link href="https://fonts.googleapis.com/css2?family=Arimo:wght@400;700&display=swap" rel="stylesheet">
<style>
  :root{
    --header-top:#2e9be6;
    --header-bottom:#1667b8;
    --header-line:#0f559c;
    --header-btn-top:#48b0f0;
    --header-btn-bottom:#1f7ccc;
    --header-btn-edge:#0f559c;
    --user-top:#1d75c4;
    --user-bottom:#125a9f;
    --side-bg:#e4e8ee;
    --side-item:#eef1f5;
    --side-item-2:#e0e5ec;
    --side-border:#cdd4dd;
    --side-text:#3d4652;
    --active-top:#2e9be6;
    --active-bottom:#1667b8;
    --sub-bg:#eaeef3;
    --sub-current:#d6e7f8;
    --accent:#1a78d0;
    --page-bg:#f5f7fa;
    --card:#ffffff;
    --card-border:#d6dbe2;
    --bar-top:#fbfcfd;
    --bar-bottom:#edf0f4;
    --text:#4f5761;
    --green:#14c08c;
    --red:#f2525b;
    --badge:#ff4d5a;
    --thumb:#6fb3ea;
    --thumb-edge:#4e9ddd;
  }
  *{box-sizing:border-box;margin:0;padding:0}
  html,body{width:1143px;height:1200px;overflow:hidden;background:var(--side-bg)}
  body{font-family:"Arimo",Arial,sans-serif;color:var(--text)}
  .stage{position:absolute;left:0;top:0;width:980px;height:1029px;transform:scale(1.16633);transform-origin:0 0;background:var(--side-bg)}

  .topbar{position:absolute;left:0;top:0;width:980px;height:60px;background:linear-gradient(var(--header-top),var(--header-bottom));border-bottom:1px solid var(--header-line)}
  .brand{position:absolute;left:12px;top:19px;font-weight:700;font-size:20px;line-height:22px;color:#fff}
  .top-btn{position:absolute;top:20px;width:31px;height:31px;border:1px solid var(--header-btn-edge);border-radius:3px;background:linear-gradient(var(--header-btn-top),var(--header-btn-bottom));display:flex;align-items:center;justify-content:center}
  .top-btn .badge{position:absolute;top:-3px;right:-12px;background:var(--badge);color:#fff;font-size:10px;font-weight:700;padding:1px 4px;border-radius:3px;line-height:12px}
  .user-box{position:absolute;left:805px;top:12px;width:165px;height:40px;border:1px solid var(--header-btn-edge);border-radius:4px;background:linear-gradient(var(--user-top),var(--user-bottom));display:flex;align-items:center;padding-left:4px}
  .avatar{width:32px;height:32px;background:linear-gradient(#f4f4f4,#d5d5d5);border-radius:2px;display:flex;align-items:flex-end;justify-content:center;overflow:hidden}
  .user-info{margin-left:10px;color:#fff;font-size:11px}
  .user-info strong{display:block;font-size:11px;margin-bottom:3px}
  .user-info span{color:#e3f1ff}
  .user-info .sep{display:inline-block;width:1px;height:11px;background:#7fbaf0;margin:0 5px;vertical-align:-1px}

  .sidebar{position:absolute;left:0;top:61px;width:210px;list-style:none;border-right:1px solid var(--side-border)}
  .nav-item{height:42px;display:flex;align-items:center;padding-left:8px;font-size:14px;font-weight:700;color:var(--side-text);background:linear-gradient(var(--side-item),var(--side-item-2));border-bottom:1px solid var(--side-border);border-top:1px solid #f7f9fb;position:relative}
  .nav-item svg{width:18px;height:18px;margin-right:11px;flex:none}
  .nav-item.is-active{background:linear-gradient(var(--active-top),var(--active-bottom));color:#fff;border-color:var(--header-line)}
  .nav-sub{height:42px;display:flex;align-items:center;padding-left:38px;font-size:14px;color:var(--side-text);background:var(--sub-bg);border-bottom:1px solid var(--side-border);border-top:1px solid #f3f5f8}
  .nav-sub.is-current{background:var(--sub-current);color:var(--accent)}
  .nav-count{position:absolute;right:12px;top:13px;font-size:11px;font-weight:400;color:#fff;background:var(--accent);border:1px solid var(--header-line);border-radius:3px;padding:1px 6px}

  .main{position:absolute;left:210px;top:60px;width:770px;height:930px;background:var(--page-bg);border-left:1px solid var(--side-border);box-shadow:0 1px 3px rgba(0,0,0,.15)}
  .stats{height:62px;background:linear-gradient(#ffffff,#eef2f6);border-bottom:1px solid var(--card-border);display:flex;align-items:center}
  .stat{display:flex;align-items:center;height:42px;padding:0 19px;border-right:1px solid #d5dbe2}
  .stat:last-child{border-right:0}
  .stat-num{font-size:36px;font-weight:700;color:#5a626c;margin-right:8px;letter-spacing:-1px}
  .stat-num.up{color:var(--green)}
  .stat-num.down{color:var(--red)}
  .stat-label{font-size:14px;line-height:16px;color:#5f6770}
  .stat-small .stat-num{font-size:17px;margin:0;letter-spacing:0}
  .stat-small{flex-direction:column;align-items:flex-start;justify-content:center}
  .stat-small .stat-label{font-size:11px;line-height:13px}

  .panel{position:absolute;background:var(--card);border:1px solid var(--card-border);border-radius:3px}
  .panel-head{height:36px;background:linear-gradient(var(--bar-top),var(--bar-bottom));border-bottom:1px solid var(--card-border);display:flex;align-items:center;font-size:12px;font-weight:700;color:#4f5761}
  .panel-icon{width:40px;height:36px;border-right:1px solid var(--card-border);display:flex;align-items:center;justify-content:center;margin-right:10px}

  .gallery{left:19px;top:82px;width:741px;height:356px}
  .thumb{position:absolute;width:160px;height:130px;border:1px solid #d0d6de;border-radius:4px;background:#fff;padding:4px}
  .thumb-fill{width:100%;height:100%;background:linear-gradient(135deg,var(--thumb),#4aa3e8);border:1px solid var(--thumb-edge)}

  .accordion{left:19px;top:458px;width:360px;height:175px;overflow:hidden}
  .acc-row{height:35px;display:flex;align-items:center;justify-content:space-between;padding:0 20px;font-size:12px;font-weight:700;color:#4f5761;background:linear-gradient(var(--bar-top),var(--bar-bottom));border-bottom:1px solid var(--card-border)}
  .acc-row.is-open{color:var(--accent);background:linear-gradient(#fdfdfe,#f1f5f9)}
  .acc-body{padding:16px 20px;font-size:12px;line-height:18px;height:69px;border-bottom:1px solid var(--card-border)}

  .tabs{left:399px;top:458px;width:361px;height:174px}
  .tab-bar{display:flex;height:36px;border-bottom:1px solid var(--card-border)}
  .tab{flex:1;display:flex;align-items:center;justify-content:center;font-size:12px;font-weight:700;color:#4f5761;background:linear-gradient(var(--bar-top),#e6eaf0);border-left:1px solid var(--card-border)}
  .tab:first-child{border-left:0}
  .tab.is-active{background:#fff;color:var(--accent);border-top:2px solid var(--accent);margin-bottom:-1px}
  .tab-body{padding:15px 19px;font-size:12px;line-height:18px}
  .tab-body p+p{margin-top:18px}

  .table-panel{left:19px;top:653px;width:741px;height:216px;overflow:hidden}
  .data-table{width:100%;border-collapse:collapse;font-size:12px;table-layout:fixed}
  .data-table th{height:30px;text-align:left;padding-left:20px;font-weight:700;color:#4f5761;background:#f4f7fa;border-bottom:1px solid var(--card-border);border-left:1px solid var(--card-border)}
  .data-table td{height:30px;padding-left:20px;color:#4f5761;border-top:1px solid #e0e5eb;border-left:1px solid var(--card-border)}
  .data-table th:first-child,.data-table td:first-child{border-left:0}
  .sort{float:right;margin-right:10px;margin-top:2px}

  .pager{position:absolute;left:292px;top:888px;display:flex;gap:8px}
  .page{width:22px;height:22px;border:1px solid #cdd4dc;border-radius:3px;background:linear-gradient(#fdfdfe,#eaeef3);font-size:12px;color:#5f6770;display:flex;align-items:center;justify-content:center}
  .page.is-current{background:linear-gradient(var(--active-top),var(--active-bottom));color:#fff;border-color:var(--header-line)}

  .footer{position:absolute;left:210px;top:1002px;font-size:11px;color:#4f5761}
</style>
</head>
<body>
<div class="stage">

  <header class="topbar">
    <div class="brand">Stratus Console</div>
    <div class="top-btn" style="left:697px">
      <svg width="16" height="15" viewBox="0 0 16 15"><path d="M8 1 L15 14 H1 Z" fill="#fff"/><rect x="7.2" y="5" width="1.6" height="5" fill="#1f7ccc"/><rect x="7.2" y="11" width="1.6" height="1.6" fill="#1f7ccc"/></svg>
      <span class="badge">21</span>
    </div>
    <div class="top-btn" style="left:744px">
      <svg width="17" height="12" viewBox="0 0 17 12"><rect x="0.5" y="0.5" width="16" height="11" fill="#fff"/><path d="M1 1 L8.5 7 L16 1" stroke="#1f7ccc" fill="none" stroke-width="1.3"/></svg>
      <span class="badge">12</span>
    </div>
    <div class="user-box">
      <div class="avatar">
        <svg width="26" height="26" viewBox="0 0 26 26"><circle cx="13" cy="10" r="6" fill="#b9b9b9"/><path d="M2 26 C2 18 24 18 24 26 Z" fill="#b9b9b9"/></svg>
      </div>
      <div class="user-info">
        <strong>Hello, John Doe</strong>
        <span>Settings</span><span class="sep"></span><span>Log Out</span>
      </div>
    </div>
  </header>

  <ul class="sidebar">
    <li class="nav-item"><svg viewBox="0 0 18 18"><circle cx="9" cy="9" r="7.5" fill="none" stroke="#1a78d0" stroke-width="1.6"/><path d="M9 9 L12.5 5" stroke="#1a78d0" stroke-width="1.6"/><circle cx="9" cy="9" r="1.6" fill="#1a78d0"/></svg>Dashboard</li>
    <li class="nav-item is-active"><svg viewBox="0 0 18 18"><path d="M1 16 H17" stroke="#fff" stroke-width="1.6"/><rect x="3" y="5" width="2" height="10" fill="#fff"/><rect x="7" y="9" width="2" height="6" fill="#fff"/><rect x="11" y="7" width="2" height="8" fill="#fff"/><rect x="15" y="11" width="2" height="4" fill="#fff"/></svg>Charts</li>
    <li class="nav-sub">Lines chart</li>
    <li class="nav-sub is-current">Vertical bars</li>
    <li class="nav-sub">Pie chart</li>
    <li class="nav-item"><svg viewBox="0 0 18 18"><path d="M9 1.5 L17 16 H1 Z" fill="#f2525b"/><rect x="8.2" y="6" width="1.6" height="5.5" fill="#fff"/><rect x="8.2" y="12.5" width="1.6" height="1.6" fill="#fff"/></svg>Notification</li>
    <li class="nav-item"><svg viewBox="0 0 18 18"><rect x="4" y="2" width="13" height="10" fill="none" stroke="#1a78d0" stroke-width="1.5"/><rect x="1" y="5" width="13" height="11" fill="#eef1f5" stroke="#1a78d0" stroke-width="1.5"/><path d="M2.5 14.5 L6 10 L9 13 L11 11 L13 14.5 Z" fill="#1a78d0"/></svg>Gallery<span class="nav-count">12</span></li>
    <li class="nav-item"><svg viewBox="0 0 18 18"><rect x="1.5" y="2.5" width="15" height="13" fill="none" stroke="#1a78d0" stroke-width="1.6"/><rect x="1.5" y="2.5" width="15" height="3" fill="#1a78d0"/><rect x="4" y="8" width="10" height="1.5" fill="#1a78d0"/><rect x="4" y="11" width="10" height="1.5" fill="#1a78d0"/></svg>Widgets</li>
    <li class="nav-item"><svg viewBox="0 0 18 18"><rect x="1" y="1" width="7" height="7" fill="#1a78d0"/><rect x="10" y="1" width="7" height="7" fill="#14c08c"/><rect x="1" y="10" width="7" height="7" fill="#14c08c"/><rect x="10" y="10" width="7" height="7" fill="#1a78d0"/></svg>Tables</li>
    <li class="nav-item"><svg viewBox="0 0 18 18"><circle cx="9" cy="9" r="7" fill="none" stroke="#1a78d0" stroke-width="1.6"/><circle cx="9" cy="9" r="2.5" fill="#1a78d0"/></svg>Buttons</li>
    <li class="nav-item"><svg viewBox="0 0 18 18"><rect x="1.5" y="3.5" width="12" height="12" fill="none" stroke="#1a78d0" stroke-width="1.6"/><path d="M7 11 L16 2" stroke="#1a78d0" stroke-width="2.5"/></svg>Form elements</li>
    <li class="nav-item"><svg viewBox="0 0 18 18"><rect x="1.5" y="3.5" width="12" height="12" fill="none" stroke="#1a78d0" stroke-width="1.6"/><path d="M6 12 L15 3" stroke="#1a78d0" stroke-width="1.6"/><path d="M4 13 L6 11" stroke="#1a78d0" stroke-width="2"/></svg>Typography</li>
  </ul>

  <main class="main">
    <section class="stats">
      <div class="stat"><span class="stat-num">23</span><span class="stat-label">Active<br>Projects</span></div>
      <div class="stat"><span class="stat-num up">+23</span><span class="stat-label">New<br>Members</span></div>
      <div class="stat"><span class="stat-num down">-7%</span><span class="stat-label" style="margin-left:10px">Unique<br>Visitors</span></div>
      <div class="stat stat-small"><span class="stat-num">1523</span><span class="stat-label">Total Visitors</span></div>
      <div class="stat stat-small"><span class="stat-num">357</span><span class="stat-label">Monthly Visitors</span></div>
    </section>

    <section class="panel gallery">
      <div class="panel-head">
        <span class="panel-icon"><svg width="18" height="16" viewBox="0 0 18 16"><rect x="4" y="1" width="13" height="10" fill="none" stroke="#1a78d0" stroke-width="1.4"/><rect x="1" y="4" width="13" height="11" fill="#f5f7fa" stroke="#1a78d0" stroke-width="1.4"/><path d="M2.5 13.5 L6 9 L9 12 L11 10 L13 13.5 Z" fill="#1a78d0"/></svg></span>Gallery
      </div>
      <div class="thumb" style="left:19px;top:55px"><div class="thumb-fill" role="img" aria-label="Gallery image placeholder"></div></div>
      <div class="thumb" style="left:199px;top:55px"><div class="thumb-fill" role="img" aria-label="Gallery image placeholder"></div></div>
      <div class="thumb" style="left:379px;top:55px"><div class="thumb-fill" role="img" aria-label="Gallery image placeholder"></div></div>
      <div class="thumb" style="left:559px;top:55px"><div class="thumb-fill" role="img" aria-label="Gallery image placeholder"></div></div>
      <div class="thumb" style="left:19px;top:205px"><div class="thumb-fill" role="img" aria-label="Gallery image placeholder"></div></div>
      <div class="thumb" style="left:199px;top:205px"><div class="thumb-fill" role="img" aria-label="Gallery image placeholder"></div></div>
      <div class="thumb" style="left:379px;top:205px"><div class="thumb-fill" role="img" aria-label="Gallery image placeholder"></div></div>
      <div class="thumb" style="left:559px;top:205px"><div class="thumb-fill" role="img" aria-label="Gallery image placeholder"></div></div>
    </section>

    <section class="panel accordion">
      <div class="acc-row is-open">Toggle active<svg width="8" height="6" viewBox="0 0 8 6"><path d="M1 1 L4 4.5 L7 1" stroke="#1a78d0" stroke-width="1.6" fill="none"/></svg></div>
      <div class="acc-body">Duis aute irure dolor in reprehenderit in voluptate velit es cillum dolore eu fugiat nulla pariatur.</div>
      <div class="acc-row">Toggle inactiv<svg width="6" height="8" viewBox="0 0 6 8"><path d="M1 1 L4.5 4 L1 7" stroke="#4f5761" stroke-width="1.6" fill="none"/></svg></div>
      <div class="acc-row">Toggle inactiv<svg width="6" height="8" viewBox="0 0 6 8"><path d="M1 1 L4.5 4 L1 7" stroke="#4f5761" stroke-width="1.6" fill="none"/></svg></div>
    </section>

    <section class="panel tabs">
      <div class="tab-bar">
        <div class="tab is-active">Tab 1</div>
        <div class="tab">Tab 2</div>
        <div class="tab">Tab 3</div>
        <div class="tab">Tab 4</div>
      </div>
      <div class="tab-body">
        <p>Lorem ipsum dolor sit amet, consectetur adipisicing elit, se do eiusmod tempor incididunt ut labore et dolore magna aliqua.</p>
        <p>Duis aute irure dolor in reprehenderit in voluptate velit esse cillum dolore eu fugiat nulla pariatur.</p>
      </div>
    </section>

    <section class="panel table-panel">
      <div class="panel-head" style="padding-left:20px">Table sample</div>
      <table class="data-table">
        <colgroup><col style="width:151px"><col style="width:151px"><col style="width:150px"><col style="width:150px"><col></colgroup>
        <thead>
          <tr><th>Column name</th><th>Column name</th><th>Column name</th><th>Column name</th><th>Last col<svg class="sort" width="8" height="11" viewBox="0 0 8 11"><path d="M4 0 L8 4 H0 Z M4 11 L0 7 H8 Z" fill="#1a78d0"/></svg></th></tr>
        </thead>
        <tbody>
          <tr><td>Row 1</td><td>Row 2</td><td>Row 3</td><td>Row 4</td><td>02-05-1900</td></tr>
          <tr><td>Row 1</td><td>Row 2</td><td>Row 3</td><td>Row 4</td><td>02-05-1900</td></tr>
          <tr><td>Row 1</td><td>Row 2</td><td>Row 3</td><td>Row 4</td><td>02-05-1900</td></tr>
          <tr><td>Row 1</td><td>Row 2</td><td>Row 3</td><td>Row 4</td><td>02-05-1900</td></tr>
          <tr><td>Row 1</td><td>Row 2</td><td>Row 3</td><td>Row 4</td><td>02-05-1900</td></tr>
        </tbody>
      </table>
    </section>

    <nav class="pager">
      <span class="page"><svg width="7" height="10" viewBox="0 0 7 10"><path d="M6 1 L2 5 L6 9" stroke="#4f5761" stroke-width="2" fill="none"/></svg></span>
      <span class="page">1</span>
      <span class="page is-current">2</span>
      <span class="page">3</span>
      <span class="page">4</span>
      <span class="page">5</span>
      <span class="page"><svg width="7" height="10" viewBox="0 0 7 10"><path d="M1 1 L5 5 L1 9" stroke="#4f5761" stroke-width="2" fill="none"/></svg></span>
    </nav>
  </main>

  <footer class="footer">© 2012 Cloudvale.net,&nbsp; All rights reserved</footer>
</div>
</body>
</html>
```